Mobile and Web design for Remote Skin Condition Service

A new web service that allows patients to upload photos for doctors to review. I need the designs for both mobile (NOT native app) and desktop versions. Key pages are provided in the mockups, and all major form elements are required.
Overall branding and design needed.

We are building an online system that allows patients to connect with a skin doctors.

Users will access the website (typically, but not exclusively via a mobile phone), register, upload photos, answer a few questions and pay to submit their details to a doctor.

The doctor will access the website via a desktop browser and review the case.

The patient’s user flow should be optimised for mobile. It should be usable on desktop too.

The doctor’s user flow should be optimised for desktop. It should be usable on mobile too.

Currently there are no branding restrictions, and no logo, so please be creative.

The site has to look professional, clean and easy to use.
There will be limited text on the pages.
Buttons should be prominent - but they should also obviously be buttons.

Attached are a selection of screens showing most of the functionality of the process - it is not all of the screens of the process but should give the developers enough range and examples.

Target Market(s)

Any user with a skin condition

Industry/Entity Type

Healthcare

Number of Pages Required

5+ page

Colors

Designer to choose colors to be used in the design.

Requirements
Must have
• Mobile and desktop versions of the key pages as per the brief.
• Should be obvious to use - eg the photo upload and camera functions should be standard

```html
<!DOCTYPE html>
<html lang="en">
<head>
<meta charset="utf-8">
<title>dermavue – Doctor Portal Screens</title>
<link href="https://fonts.googleapis.com/css2?family=Nunito+Sans:wght@400;600;700&display=swap" rel="stylesheet">
<style>
:root{
  --board:#0e3a45;
  --brand:#2b86b3;
  --teal-dark:#15667a;
  --teal-light:#36b1bf;
  --heading:#1b6b80;
  --label:#2d86b0;
  --text:#3a4650;
  --line:#b7c6d2;
  --input-border:#aab7c4;
  --row-alt:#f1f5f9;
  --panel-head:#176e7f;
  --sky-top:#f6fafd;
  --sky-bottom:#c3e2f2;
}
*{box-sizing:border-box;margin:0;padding:0}
html,body{width:1200px;height:2589px;overflow:hidden}
body{background:var(--board);font-family:"Nunito Sans",sans-serif;color:var(--text);position:relative}
.screen{position:absolute;left:89px;width:1037px;overflow:hidden}
.abs{position:absolute}
.brand{font-weight:600;font-size:41px;color:var(--brand);letter-spacing:.5px;width:100%;text-align:center;line-height:1}

/* login */
.screen-login{top:52px;height:720px;background:linear-gradient(160deg,#f7fbfe 0%,#d9eef8 55%,#9fd0ec 100%)}
.helix-art{left:110px;top:60px;width:420px;height:660px;background:radial-gradient(ellipse at 50% 60%,rgba(180,225,245,.7),rgba(200,232,247,0) 70%)}
.login-card{left:323px;top:160px;width:385px;height:403px;background:#fff;box-shadow:0 2px 6px rgba(0,0,0,.08)}
.login-title{top:35px;width:100%;text-align:center;font-size:26px;font-weight:600;color:var(--label)}
.field-label{font-size:15px;color:var(--label)}
.pill-input{border:1px solid var(--input-border);border-radius:23px;height:45px;background:#fff;font-size:11px;color:var(--brand);padding-left:20px;display:flex;align-items:center}
.btn{border-radius:30px;background:linear-gradient(90deg,var(--teal-dark),var(--teal-light));color:#fff;font-weight:700;display:flex;align-items:center;justify-content:center}
.btn-login{left:35px;top:273px;width:311px;height:55px;font-size:20px}
.forgot{right:45px;top:346px;font-size:12px;color:var(--brand)}
.footer-rule{left:85px;width:850px;height:1px;background:#9db3c1}
.footer-text{width:100%;text-align:center;font-size:12.5px;color:#2e3d48}

/* shared header */
.topbar{left:0;top:0;width:100%;height:86px;background:#fff;border-bottom:2px solid #e4ebf0}
.topbar .brand{position:absolute;top:18px}
.nav-link{font-size:14px;font-weight:700;color:var(--heading);display:flex;align-items:center;gap:5px}
.page-title{width:100%;text-align:center;font-size:28px;font-weight:600;color:var(--heading)}
.inner-bg{background:linear-gradient(180deg,var(--sky-top) 0%,#e4f1f9 45%,var(--sky-bottom) 100%)}

/* account */
.screen-account{top:822px;height:719px}
.account-card{left:119px;top:180px;width:797px;height:417px;background:#fff;box-shadow:0 1px 4px rgba(0,0,0,.1)}
.box-input{width:306px;height:39px;border:1px solid var(--input-border);background:#fff}
.section-title{font-size:20px;font-weight:600;color:var(--label)}
.btn-small{width:150px;height:39px;font-size:13.5px}

/* dashboard */
.screen-dashboard{top:1588px;height:903px}
.panel{background:#fff;box-shadow:0 1px 4px rgba(0,0,0,.1)}
.panel-new{left:118px;top:187px;width:404px;height:282px}
.panel-closed{left:544px;top:187px;width:404px;height:282px}
.panel-head{height:46px;background:var(--panel-head);color:#fff;font-size:20px;font-weight:600;padding:11px 0 0 22px}
.col-head{top:61px;font-size:13px;color:var(--label)}
.chev{width:11px;height:7px;top:66px}
.row{left:0;width:100%;height:30px;font-size:12px;color:#3c4751}
.row.alt{background:var(--row-alt)}
.row span{position:absolute;top:7px}
.panel-search{left:118px;top:490px;width:830px;height:321px}
.search-title{left:38px;top:36px;font-size:20px;font-weight:600;color:var(--heading)}
.search-label{left:40px;font-size:13.5px;color:#2e3d48}
.search-input{height:32px;border:1px solid #9fc6d8;background:#eef5fa;border-radius:17px;font-size:10px;color:#4a5660;display:flex;align-items:center}
.date-input{width:92px;padding-left:12px;gap:4px}
.btn-search{left:42px;top:268px;width:114px;height:30px;font-size:14px}
.results{left:430px;top:44px;width:382px;height:230px;border:1px solid #dde5ec}
</style>
</head>
<body>

<!-- Login screen -->
<section class="screen screen-login">
  <div class="abs helix-art" role="img" aria-label="Faint DNA helix background illustration"></div>
  <div class="abs brand" style="top:34px">dermavue</div>
  <div class="abs login-card">
    <h1 class="abs login-title">Doctor Login</h1>
    <div class="abs field-label" style="left:39px;top:91px">Email address</div>
    <div class="abs pill-input" style="left:35px;top:118px;width:316px">doctor@clinicmail.test</div>
    <div class="abs field-label" style="left:39px;top:184px">Password</div>
    <div class="abs pill-input" style="left:37px;top:210px;width:316px;letter-spacing:1px">*****************</div>
    <div class="abs btn btn-login">Login</div>
    <div class="abs forgot">Forgotten Password?</div>
  </div>
  <div class="abs footer-rule" style="top:651px"></div>
  <div class="abs footer-text" style="top:666px">© 2020 Company Name | All Rights Reserved | Disclaimer</div>
</section>

<!-- My Account screen -->
<section class="screen screen-account inner-bg">
  <header class="abs topbar">
    <div class="brand">dermavue</div>
    <div class="abs nav-link" style="left:825px;top:33px">
      <svg width="20" height="20" viewBox="0 0 20 20" fill="none" stroke="#1b6b80" stroke-width="1.5"><circle cx="10" cy="10" r="8.5"/><path d="M10 1.5v9M10 10.5l-6 6M10 10.5l6 6M6 4l4 6.5 4-6.5"/></svg>
      Dashboard
    </div>
  </header>
  <h1 class="abs page-title" style="top:113px">My Account</h1>
  <div class="abs account-card">
    <div class="abs field-label" style="left:44px;top:26px">Name</div>
    <div class="abs box-input" style="left:44px;top:50px"></div>
    <div class="abs field-label" style="left:44px;top:106px">Email</div>
    <div class="abs box-input" style="left:44px;top:129px"></div>
    <div class="abs field-label" style="left:44px;top:186px">GMC Number</div>
    <div class="abs box-input" style="left:47px;top:211px"></div>
    <div class="abs field-label" style="left:44px;top:266px">Mobile Phone Number</div>
    <div class="abs box-input" style="left:47px;top:292px"></div>
    <div class="abs btn btn-small" style="left:50px;top:345px">Update Details</div>

    <h2 class="abs section-title" style="left:430px;top:58px">Change Password</h2>
    <div class="abs field-label" style="left:437px;top:100px">Old Password</div>
    <div class="abs box-input" style="left:435px;top:125px"></div>
    <div class="abs field-label" style="left:437px;top:180px">New Password</div>
    <div class="abs box-input" style="left:435px;top:204px"></div>
    <div class="abs field-label" style="left:437px;top:260px">Confirm Password</div>
    <div class="abs box-input" style="left:435px;top:286px"></div>
    <div class="abs btn btn-small" style="left:435px;top:346px">Update Password</div>
  </div>
  <div class="abs footer-rule" style="top:651px"></div>
  <div class="abs footer-text" style="top:667px">© 2020 Company Name | All Rights Reserved | Disclaimer</div>
</section>

<!-- Medical Dashboard screen -->
<section class="screen screen-dashboard inner-bg">
  <header class="abs topbar">
    <div class="brand">dermavue</div>
    <div class="abs nav-link" style="left:845px;top:33px">
      <svg width="18" height="20" viewBox="0 0 18 20" fill="none" stroke="#1b6b80" stroke-width="1.5"><circle cx="9" cy="6" r="4.5"/><path d="M1.5 19v-2.5a4.5 4.5 0 0 1 4.5-4.5h6a4.5 4.5 0 0 1 4.5 4.5V19z"/></svg>
      My Account
    </div>
  </header>
  <h1 class="abs page-title" style="top:112px">Medical Dashboard</h1>

  <div class="abs panel panel-new">
    <div class="panel-head">New Cases</div>
    <div class="abs col-head" style="left:29px">Case ID</div>
    <div class="abs col-head" style="left:89px">Name</div>
    <svg class="abs chev" style="left:190px" viewBox="0 0 11 7"><path d="M1 1l4.5 4.5L10 1" fill="none" stroke="#1b6b80" stroke-width="1.6"/></svg>
    <div class="abs col-head" style="left:211px">Date Submitted</div>
    <svg class="abs chev" style="left:304px" viewBox="0 0 11 7"><path d="M1 1l4.5 4.5L10 1" fill="none" stroke="#1b6b80" stroke-width="1.6"/></svg>
    <div class="abs col-head" style="left:324px">Locked by</div>
    <div class="abs row alt" style="top:83px"><span style="left:30px">2545</span><span style="left:90px">Mira Ostrand</span><span style="left:215px">23 Nov 14:17</span><span style="left:322px">Open</span></div>
    <div class="abs row" style="top:113px"><span style="left:30px">2533</span><span style="left:90px">Jalen Pryce</span><span style="left:215px">23 Nov 14:19</span><span style="left:322px">Open</span></div>
    <div class="abs row alt" style="top:143px"><span style="left:30px">2566</span><span style="left:90px">Nola Beckett</span><span style="left:215px">23 Nov 15:45</span><span style="left:322px">Dr Hale</span></div>
    <div class="abs row" style="top:173px"><span style="left:30px">2523</span><span style="left:90px">Corinne Vasquel</span><span style="left:215px">23 Nov 14:17</span><span style="left:322px">Dr Penrose</span></div>
    <div class="abs row alt" style="top:203px"><span style="left:30px">2567</span><span style="left:90px">Hollis Marrow</span><span style="left:215px">23 Nov 14:17</span><span style="left:322px">Dr Ashby</span></div>
    <div class="abs row" style="top:233px"><span style="left:30px">2534</span><span style="left:90px">Teo Brannick</span><span style="left:215px">23 Nov 14:17</span><span style="left:322px">Dr Rowe</span></div>
  </div>

  <div class="abs panel panel-closed">
    <div class="panel-head">Recently Closed Cases</div>
    <div class="abs col-head" style="left:29px">Case ID</div>
    <div class="abs col-head" style="left:89px">Name</div>
    <svg class="abs chev" style="left:190px" viewBox="0 0 11 7"><path d="M1 1l4.5 4.5L10 1" fill="none" stroke="#1b6b80" stroke-width="1.6"/></svg>
    <div class="abs col-head" style="left:211px">Date Closed</div>
    <svg class="abs chev" style="left:304px" viewBox="0 0 11 7"><path d="M1 1l4.5 4.5L10 1" fill="none" stroke="#1b6b80" stroke-width="1.6"/></svg>
    <div class="abs col-head" style="left:324px">Doctor</div>
    <div class="abs row alt" style="top:83px"><span style="left:30px">2545</span><span style="left:90px">Mira Ostrand</span><span style="left:215px">23 Nov 14:17</span><span style="left:322px">Dr Hale</span></div>
    <div class="abs row" style="top:113px"><span style="left:30px">2533</span><span style="left:90px">Jalen Pryce</span><span style="left:215px">23 Nov 14:19</span><span style="left:322px">Dr Hale</span></div>
    <div class="abs row alt" style="top:143px"><span style="left:30px">2566</span><span style="left:90px">Nola Beckett</span><span style="left:215px">23 Nov 15:45</span><span style="left:322px">Dr Hale</span></div>
    <div class="abs row" style="top:173px"><span style="left:30px">2523</span><span style="left:90px">Corinne Vasquel</span><span style="left:215px">23 Nov 14:17</span><span style="left:322px">Dr Penrose</span></div>
    <div class="abs row alt" style="top:203px"><span style="left:30px">2567</span><span style="left:90px">Hollis Marrow</span><span style="left:215px">23 Nov 16:17</span><span style="left:322px">Dr Ashby</span></div>
    <div class="abs row" style="top:233px"><span style="left:30px">2534</span><span style="left:90px">Teo Brannick</span><span style="left:215px">23 Nov 19:17</span><span style="left:322px">Dr Rowe</span></div>
  </div>

  <div class="abs panel panel-search">
    <h2 class="abs search-title">Search by Cases</h2>
    <div class="abs search-label" style="top:84px">Patient Surname</div>
    <div class="abs search-input" style="left:177px;top:77px;width:198px;padding-left:32px">Search by name</div>
    <div class="abs search-label" style="top:127px">Doctor Name</div>
    <div class="abs search-input" style="left:178px;top:119px;width:198px;padding-left:30px">Search by Dr name</div>
    <div class="abs search-label" style="top:170px">Submitted Between</div>
    <div class="abs search-input date-input" style="left:178px;top:159px"><svg width="11" height="11" viewBox="0 0 11 11"><rect x=".5" y="1.5" width="10" height="9" fill="none" stroke="#2d86b0"/><path d="M.5 4h10M3 0v3M8 0v3M3 6h1M5 6h1M7 6h1M3 8h1M5 8h1M7 8h1" stroke="#2d86b0"/></svg>25 /12/19</div>
    <div class="abs search-input date-input" style="left:275px;top:159px"><svg width="11" height="11" viewBox="0 0 11 11"><rect x=".5" y="1.5" width="10" height="9" fill="none" stroke="#2d86b0"/><path d="M.5 4h10M3 0v3M8 0v3M3 6h1M5 6h1M7 6h1M3 8h1M5 8h1M7 8h1" stroke="#2d86b0"/></svg>25 /12/19</div>
    <div class="abs search-label" style="top:213px">Closed Between</div>
    <div class="abs search-input date-input" style="left:179px;top:201px"><svg width="11" height="11" viewBox="0 0 11 11"><rect x=".5" y="1.5" width="10" height="9" fill="none" stroke="#2d86b0"/><path d="M.5 4h10M3 0v3M8 0v3M3 6h1M5 6h1M7 6h1M3 8h1M5 8h1M7 8h1" stroke="#2d86b0"/></svg>25 /12/19</div>
    <div class="abs search-input date-input" style="left:276px;top:201px"><svg width="11" height="11" viewBox="0 0 11 11"><rect x=".5" y="1.5" width="10" height="9" fill="none" stroke="#2d86b0"/><path d="M.5 4h10M3 0v3M8 0v3M3 6h1M5 6h1M7 6h1M3 8h1M5 8h1M7 8h1" stroke="#2d86b0"/></svg>25 /12/19</div>
    <div class="abs btn btn-search">Search</div>

    <div class="abs results">
      <div class="abs col-head" style="left:22px;top:20px">Case ID</div>
      <div class="abs col-head" style="left:80px;top:20px">Name</div>
      <svg class="abs chev" style="left:180px;top:25px" viewBox="0 0 11 7"><path d="M1 1l4.5 4.5L10 1" fill="none" stroke="#1b6b80" stroke-width="1.6"/></svg>
      <div class="abs col-head" style="left:200px;top:20px">Date Closed</div>
      <svg class="abs chev" style="left:291px;top:25px" viewBox="0 0 11 7"><path d="M1 1l4.5 4.5L10 1" fill="none" stroke="#1b6b80" stroke-width="1.6"/></svg>
      <div class="abs col-head" style="left:310px;top:20px">Doctor</div>
      <div class="abs row alt" style="top:40px"><span style="left:23px">2545</span><span style="left:81px">Mira Ostrand</span><span style="left:204px">23 Nov 14:17</span><span style="left:309px">Dr Hale</span></div>
      <div class="abs row" style="top:70px"></div>
      <div class="abs row alt" style="top:100px"></div>
      <div class="abs row" style="top:130px"></div>
      <div class="abs row alt" style="top:160px"></div>
    </div>
  </div>

  <div class="abs footer-rule" style="left:93px;top:843px"></div>
  <div class="abs footer-text" style="left:8px;top:858px">© 2020 Company Name | All Rights Reserved | Disclaimer</div>
</section>

</body>
</html>
```